Bluebird Listings ad 2014 15

I need a design for an advertisement in our Bluebird Listings book telephone directory.
The directory runs for a 12 month period.

Our business offers 24 hour glass replacements to homes, shops and offices.
Our service is usually required by customers that require their glass replaced urgently
.
The ad is 1 of many in the directory offering the same service so we need to attract the customers attention quickly and easily and deliver our message - "24hr glass replacements to doors windows and shopfronts. Call now 9372 4816".

I want to keep the data in the attached ad but with a professional graphic presentation.

The ad size is 58mm high x 83mm wide, full colour.

Target Market(s)

Our customer is generally someone in need of an emergency repair. They aren't spending time shopping around for a product, they have a problem that they want fixed promptly and professionally.

Industry/Entity Type

Business

Font styles to use
Sans Serif

Colors
0255a3
f37022

Requirements
Must have
• "24HR" must stand out, this is a key aspect of our service. The ad needs to be clear and easy to read.

```html
<!DOCTYPE html>
<html lang="en">
<head>
<meta charset="utf-8">
<title>Clearway Glass – 24hr Glass Replacement</title>
<link rel="stylesheet" href="https://fonts.googleapis.com/css2?family=Orbitron:wght@900&family=Cinzel:wght@400&family=Arimo:wght@400;700&family=Cardo:wght@400&family=Cormorant+Garamond:ital,wght@1,700&display=swap">
<style>
  :root {
    --ink: #0d0d0d;
    --glass-dark: #1a1a1a;
    --glass-mid: #3a3a3a;
    --white: #ffffff;
    --blue: #0255a3;
    --orange: #f37022;
    --red: #d9261c;
    --yellow: #fff47a;
    --icon-grey: #e6e6e6;
  }
  * { box-sizing: border-box; margin: 0; padding: 0; }
  html, body { width: 1200px; height: 839px; overflow: hidden; background: var(--ink); }
  .ad {
    position: relative;
    width: 1200px;
    height: 839px;
    overflow: hidden;
    color: var(--white);
    font-family: "Arimo", Arial, sans-serif;
  }
  .ad__backdrop {
    position: absolute; inset: 0;
    background: radial-gradient(ellipse at 62% 30%, var(--glass-mid) 0%, var(--glass-dark) 45%, var(--ink) 100%);
  }
  .headline { position: absolute; left: 70px; top: 26px; width: 890px; height: 116px; }
  .headline text {
    font-family: "Orbitron", sans-serif;
    font-weight: 900;
    font-size: 112px;
    fill: var(--white);
  }
  .question-mark {
    position: absolute; left: 998px; top: 37px; width: 116px; height: 165px;
    background: linear-gradient(180deg, #f2f2f2 0%, #bdbdbd 100%);
    border-radius: 40px 40px 20px 20px;
    opacity: .85;
  }
  .tagline {
    position: absolute; left: 200px; top: 146px; width: 740px;
    font-family: "Cinzel", serif; font-size: 48px; letter-spacing: 1px;
    text-align: center; white-space: nowrap;
  }
  .hours { position: absolute; left: 55px; top: 300px; width: 232px; height: 539px; }
  .hours__panel { position: absolute; left: 0; top: 0; }
  .hours__num, .hours__unit {
    position: absolute; left: 0; width: 232px; text-align: center;
    font-weight: 700; line-height: 1;
  }
  .hours__num { top: 110px; font-size: 178px; letter-spacing: -8px; color: var(--blue); }
  .hours__unit { top: 300px; font-size: 134px; color: var(--orange); letter-spacing: -2px; }
  .services { list-style: none; }
  .services__item {
    position: absolute; display: flex; align-items: center; gap: 20px;
    font-weight: 700; font-size: 42px; white-space: nowrap; line-height: 1;
  }
  .services__icon { width: 40px; height: 40px; flex: none; }
  .brand { position: absolute; left: 866px; top: 316px; width: 320px; text-align: center; }
  .brand__name { font-weight: 700; font-size: 36px; line-height: 40px; }
  .brand__slogan { font-size: 33px; line-height: 40px; margin-top: 2px; }
  .promise {
    position: absolute; left: 356px; top: 526px; width: 720px;
    font-family: "Cardo", serif; font-size: 40px; line-height: 48px; text-align: center;
  }
  .call {
    position: absolute; left: 316px; top: 644px; width: 800px;
    font-weight: 700; font-size: 78px; color: var(--red); text-align: center;
    line-height: 1; white-space: nowrap;
  }
  .guarantee {
    position: absolute; left: 316px; top: 722px; width: 800px;
    font-family: "Cormorant Garamond", serif; font-style: italic; font-weight: 700;
    font-size: 36px; text-align: center; white-space: nowrap;
  }
  .insurance {
    position: absolute; left: 316px; top: 784px; width: 840px; height: 48px;
    display: flex; align-items: center; justify-content: center; gap: 18px;
  }
  .insurance__text { font-weight: 700; font-size: 37px; white-space: nowrap; }
  .insurance__arrow { width: 164px; height: 30px; flex: none; }
</style>
</head>
<body>
<main class="ad">
  <div class="ad__backdrop" role="img" aria-label="Photograph of shattered glass with radiating cracks on black"></div>

  <svg class="headline" viewBox="0 0 890 116" aria-label="broken glass">
    <text x="2" y="92" textLength="884" lengthAdjust="spacingAndGlyphs">broken glass</text>
  </svg>
  <div class="question-mark" role="img" aria-label="Hand-brushed white question mark"></div>

  <p class="tagline">WE CAN REPLACE IT</p>

  <section class="hours" aria-label="24 hour service">
    <svg class="hours__panel" width="232" height="539" viewBox="0 0 232 539" aria-hidden="true">
      <path d="M0 60 Q116 20 232 60 L232 539 L0 539 Z" fill="var(--yellow)"/>
    </svg>
    <span class="hours__num">24</span>
    <span class="hours__unit">HR</span>
  </section>

  <ul class="services">
    <li class="services__item" style="left:320px; top:232px;"><svg class="services__icon" viewBox="0 0 40 40" aria-hidden="true"><circle cx="20" cy="20" r="19" fill="var(--orange)"/><path d="M11 21 L17 27 L29 13" fill="none" stroke="#fff" stroke-width="5" stroke-linecap="round" stroke-linejoin="round"/></svg>DOOR GLASS</li>
    <li class="services__item" style="left:362px; top:296px;"><svg class="services__icon" viewBox="0 0 40 40" aria-hidden="true"><circle cx="20" cy="20" r="19" fill="var(--orange)"/><path d="M11 21 L17 27 L29 13" fill="none" stroke="#fff" stroke-width="5" stroke-linecap="round" stroke-linejoin="round"/></svg>WINDOW GLASS</li>
    <li class="services__item" style="left:368px; top:360px;"><svg class="services__icon" viewBox="0 0 40 40" aria-hidden="true"><circle cx="20" cy="20" r="19" fill="var(--orange)"/><path d="M11 21 L17 27 L29 13" fill="none" stroke="#fff" stroke-width="5" stroke-linecap="round" stroke-linejoin="round"/></svg>SHOWER GLASS</li>
    <li class="services__item" style="left:316px; top:428px;"><svg class="services__icon" viewBox="0 0 40 40" aria-hidden="true"><circle cx="20" cy="20" r="19" fill="var(--orange)"/><path d="M11 21 L17 27 L29 13" fill="none" stroke="#fff" stroke-width="5" stroke-linecap="round" stroke-linejoin="round"/></svg>SHOPFRONT GLASS</li>
  </ul>

  <div class="brand">
    <p class="brand__name">CLEARWAY<br>GLASS</p>
    <p class="brand__slogan">The trusted name in<br>glass replacement</p>
  </div>

  <p class="promise">To regain the safety and security<br>in your home, shop or office</p>

  <p class="call">Call : 9372 4816</p>

  <p class="guarantee">Qualified tradesman. All work Guaranteed</p>

  <div class="insurance">
    <svg class="insurance__arrow" viewBox="0 0 164 30" aria-hidden="true">
      <path d="M0 3 L34 3 L46 15 L34 27 L0 27 L12 15 Z" fill="var(--orange)"/>
      <line x1="50" y1="15" x2="146" y2="15" stroke="var(--orange)" stroke-width="3" stroke-dasharray="9 6"/>
      <path d="M140 6 L164 15 L140 24 Z" fill="var(--orange)"/>
    </svg>
    <span class="insurance__text">Insurance billed Direct</span>
    <svg class="insurance__arrow" viewBox="0 0 164 30" aria-hidden="true">
      <path d="M164 3 L130 3 L118 15 L130 27 L164 27 L152 15 Z" fill="var(--orange)"/>
      <line x1="114" y1="15" x2="18" y2="15" stroke="var(--orange)" stroke-width="3" stroke-dasharray="9 6"/>
      <path d="M24 6 L0 15 L24 24 Z" fill="var(--orange)"/>
    </svg>
  </div>
</main>
</body>
</html>
```